Trifold Brochure

This is relatively easy. We already have a trifold made we simply want to update the LOOK to look more like our current website. All content would stay the same the only thing that would change would be the fonts, colors and background images to match the current website.

I have attached a word doc of the old trifold brochure. We would want the content to remain on the same pages of the trifold. Again all you are doing is updating the font, logo, colors and any background images. Please comment with any questions.

This is a 5 day project!

Requirements
Must have
• Logo, colors and fonts to match our current website.
http://www.brackenfieldworks.example/

```html
<!DOCTYPE html>
<html lang="en">
<head>
<meta charset="utf-8">
<title>Brackenfield Structural Works – Trifold Brochure</title>
<link rel="stylesheet" href="https://fonts.googleapis.com/css2?family=Ubuntu:wght@700&family=PT+Sans+Narrow:wght@400;700&display=swap">
<style>
  :root{
    --canvas:#e6e6e6;
    --green-dark:#4e6b1c;
    --green-mid:#6d8b30;
    --green-soft:#9fb56a;
    --green-pale:#c8d6a2;
    --green-wash:#e9efd8;
    --slate:#3d4a4e;
    --teal:#84ddd3;
    --text-green:#4a6712;
    --text-body:#2b2b2b;
    --paper:#f4f4f2;
  }
  *{box-sizing:border-box;margin:0;padding:0}
  html,body{width:1200px;height:1080px;overflow:hidden}
  body{background:var(--canvas);font-family:"PT Sans Narrow",sans-serif;color:var(--text-body)}
  .brochure{position:absolute;left:42px;top:96px;width:1116px;height:888px;display:flex;box-shadow:0 6px 24px rgba(0,0,0,.18)}
  .panel{position:relative;width:372px;height:100%;overflow:hidden;background:var(--paper)}

  /* Left panel */
  .panel--who{background:var(--green-wash)}
  .who__photo{position:absolute;left:0;top:0;width:124px;height:100%;background:linear-gradient(180deg,#8ea55a 0%,#7a9544 45%,#5f7c2a 100%)}
  .who__column{position:absolute;left:124px;top:170px;width:248px;bottom:0;background:linear-gradient(180deg,#eef2e2,#e2e9cc)}
  .who__head{position:absolute;left:0;top:0;width:372px;height:220px}
  .who__title{position:absolute;left:52px;top:30px;font-family:"Ubuntu",sans-serif;font-weight:700;font-size:30px;color:#fff;letter-spacing:.3px}
  .who__tabs{position:absolute;left:124px;top:186px;display:flex;height:20px}
  .who__tabs span{display:block;height:100%}
  .who__body{position:absolute;left:140px;top:224px;width:218px;color:var(--text-green)}
  .who__body h2{font-weight:400;font-size:17px;margin-bottom:14px}
  .who__list{list-style:none;font-size:11.5px;line-height:1.36}
  .who__list li{position:relative;padding-left:11px;margin-bottom:9px}
  .who__list li::before{content:"";position:absolute;left:0;top:6px;width:3px;height:3px;background:var(--text-green)}
  .who__flex{margin-top:14px;font-size:11.5px;line-height:1.36}
  .who__checks{position:absolute;left:18px;top:560px}
  .who__checks svg{display:block;margin-bottom:40px}

  /* Middle panel */
  .panel--inside{background:var(--paper)}
  .inside__band{position:absolute;left:0;top:0;width:100%;height:120px}
  .inside__contact{position:absolute;left:20px;top:82px;display:flex;gap:16px;align-items:flex-start}
  .brand-mark{width:62px;height:62px;background:var(--green-mid);flex:none}
  .inside__address{font-size:12px;line-height:1.38;color:#333;padding-top:6px}
  .inside__address .brand-name{font-size:12px}
  .inside__address b{font-weight:700}
  .inside__address a{color:#333}
  .inside__copy{position:absolute;left:18px;top:182px;width:336px;font-size:11.2px;line-height:1.36;text-align:justify}
  .inside__copy h3{font-size:12.5px;font-weight:700;margin:18px 0 4px;text-transform:uppercase;letter-spacing:.1px}
  .inside__copy p{margin:0}

  /* Right panel */
  .panel--standards{background:var(--paper)}
  .standards__band{position:absolute;left:0;top:0;width:100%;height:120px}
  .standards__grid{position:absolute;left:0;top:150px;width:190px;height:340px;opacity:.35;background:linear-gradient(135deg,#d8dcd0,#c2c8b8)}
  .standards__strip{position:absolute;right:0;top:88px;width:172px;bottom:0;background:linear-gradient(180deg,#c9d79d 0%,#bfcf8d 70%,#aeb98c 100%)}
  .standards__body{position:relative;margin:190px 0 0 12px;width:176px;color:var(--text-green);font-size:10.4px;line-height:1.36}
  .standards__body h2{font-size:13px;font-weight:700;line-height:1.3;margin-bottom:10px}
  .standards__list{list-style:none;counter-reset:n}
  .standards__list>li{counter-increment:n;position:relative;padding-left:12px;margin-bottom:8px}
  .standards__list>li::before{content:counter(n) ".";position:absolute;left:0;font-weight:700}
  .standards__sub{list-style:none;margin-top:4px}
  .standards__sub li{margin-bottom:6px}
  .standards__foot{margin-top:16px;text-align:center;font-size:10.4px;line-height:1.45}
  .standards__foot .web{font-size:12px}
</style>
</head>
<body>
<main class="brochure">

  <!-- Panel 1: Who We Are -->
  <section class="panel panel--who">
    <div class="who__photo" role="img" aria-label="Photo of the composite piling collar and cap components over a building facade"></div>
    <div class="who__column"></div>
    <svg class="who__head" viewBox="0 0 372 220" aria-hidden="true">
      <polygon points="0,0 254,0 60,210 0,150" fill="var(--slate)" opacity=".92"/>
      <polygon points="254,0 264,0 264,120 160,172 150,110" fill="var(--teal)"/>
      <polygon points="150,110 264,120 160,172" fill="#a9ebe3"/>
    </svg>
    <h1 class="who__title">Who We Are</h1>
    <div class="who__tabs" aria-hidden="true">
      <span style="width:36px;background:#dfe7c9"></span>
      <span style="width:50px;background:#c9d6a6"></span>
      <span style="width:50px;background:#a9bd7a"></span>
      <span style="width:112px;background:var(--green-mid)"></span>
    </div>
    <div class="who__body">
      <h2>Our System includes:</h2>
      <ul class="who__list">
        <li>Collar cut to customer length in sizes ranging from 12" to 144".</li>
        <li>Collar Cap with galvanized steel u-bolts to connect to the structure.</li>
        <li>Collar spacers to allow for variations in Piling diameter.</li>
        <li>Collar Cap spacers to allow for variations in Piling diameter.</li>
        <li>Tubes of high strength adhesive glue to connect the Piling to the Collar and for the Collar flange and to fill gaps between the Piling and the Collar due to the nature of irregular Pilings.</li>
        <li>Detailed installation manual providing guidance to the installation contractor.</li>
        <li>Detailed written specifications provided in paper format and available in word format upon request.</li>
      </ul>
      <p class="who__flex">Flexibility:<br>Our system has been designed to accommodate piles ranging in diameter from 8" to 12". The system can also correct vertical alignments by up to 6 degrees.</p>
    </div>
    <div class="who__checks" aria-hidden="true">
      <svg width="20" height="16" viewBox="0 0 20 16"><path d="M2 8 L8 14 L18 2" fill="none" stroke="#4fc23a" stroke-width="3.4"/></svg>
      <svg width="20" height="16" viewBox="0 0 20 16"><path d="M2 8 L8 14 L18 2" fill="none" stroke="#4fc23a" stroke-width="3.4"/></svg>
      <svg width="20" height="16" viewBox="0 0 20 16"><path d="M2 8 L8 14 L18 2" fill="none" stroke="#4fc23a" stroke-width="3.4"/></svg>
      <svg width="20" height="16" viewBox="0 0 20 16"><path d="M2 8 L8 14 L18 2" fill="none" stroke="#4fc23a" stroke-width="3.4"/></svg>
    </div>
  </section>

  <!-- Panel 2: Inside copy -->
  <section class="panel panel--inside">
    <svg class="inside__band" viewBox="0 0 372 120" preserveAspectRatio="none" aria-hidden="true">
      <path d="M0 0 H372 V86 Q186 62 0 98 Z" fill="var(--green-soft)"/>
      <path d="M160 0 H372 V60 Q270 48 160 70 Z" fill="var(--green-dark)"/>
    </svg>
    <div class="inside__contact">
      <div class="brand-mark" aria-hidden="true"></div>
      <p class="inside__address">
        <span class="brand-name">Brackenfield Structural Works, LLC</span><br>
        PO Box 41920,<br>
        Harrow Ridge, PA 18990<br>
        <b>Email:</b> <a href="mailto:sales@brackenfieldworks.example">sales@brackenfieldworks.example</a>&nbsp; <a href="http://www.brackenfieldworks.example/">www.brackenfieldworks.example</a>
      </p>
    </div>
    <div class="inside__copy">
      <p>Our Patented Piling system has been designed to withstand the corrosive environment of beach communities. The salt water and windblown sand corrodes unprotected materials, and yes, even stainless steel. Our system utilizes a high strength carbon fiber material that is corrosion proof from salt water and UV proof. The system will not erode, decay or loose strength over time. The system has three installation conditions, for raising a house on existing pilings, repairing damaged pilings, and for connecting new pilings to floor joists in new construction. The three options are generally described below:</p>
      <h3>Raising a Structure</h3>
      <p>A house on pilings can be raised by disconnecting the house from the pilings, raise the house to create a work area, cut all of the piles to a preset elevation, and install the Collar on the piling. The Collar is connected to the piling by six galvanized lag bolts and is glued with a high strength adhesive and all gaps are filled with flowable epoxy fill and fiber. The Collar extends above the piling to the bottom of the home's joists to the preset height, up to 6'-6", or higher when lateral supports are considered. Once the Collar is set on the home, it is filled with concrete to transfer the load of the house from the floor joists directly to the top of the piling, the concrete provides the compressive strength, while the Collar provides tensile and shear strength. A Collar Cap is then installed with two galvanized steel u-bolts which extend into the floor joists for the installer to connect to the joists.</p>
      <h3>Piling Repairs and Extensions</h3>
      <p>A 36" section of Collar can be installed onto an existing piling and a new section of piling can be placed on top, with 18" of the Collar covering the top of the existing and 18" covering the bottom of the new piling. Generally, the minimum length of the new piling needs to be 6 feet to ensure the piling length is not too short, which could lead to reduced piling loading capacity. This option generally requires lateral support of the pilings. Consult with your design professional</p>
      <h3>New Construction</h3>
      <p>The standard practice for connecting pilings to floor joists is to notch the pilings and bolt the joists to the pilings. This method dramatically reduces the strength of the piling due to reduced cross sectional area at the connection point. Additionally, this connection method exposes more surface area of the piling allowing for additional potential for dry rot. A 12" Collar section with a Collar Cap can be used to connect directly to the top of the new piling providing a connection that will outlast the piling by literally thousands of years.</p>
    </div>
  </section>

  <!-- Panel 3: Standards -->
  <section class="panel panel--standards">
    <svg class="standards__band" viewBox="0 0 372 120" preserveAspectRatio="none" aria-hidden="true">
      <path d="M0 0 H372 V88 Q200 50 0 68 Z" fill="var(--green-dark)"/>
    </svg>
    <div class="standards__grid" role="img" aria-label="Faint technical drawing of piling framing in the background"></div>
    <div class="standards__strip" role="img" aria-label="Light green wood grain and stone texture"></div>
    <div class="standards__body">
      <h2>General Performance<br>&nbsp;&nbsp;&nbsp;Standards, Notes and Guidance:</h2>
      <ol class="standards__list">
        <li>General Performance Standards:
          <ul class="standards__sub">
            <li>a. Vertical loading (vertical compression) 90 Kips</li>
            <li>b. Bending moment 35 ft-Kips</li>
            <li>c. Shear (lateral forces) 10 Kips.</li>
            <li>d. Alignment/plumbness correction 6 Deg.</li>
          </ul>
        </li>
        <li>This document and information provided is the property of BSW and shall not be altered, used or referenced by any third party without the expressed written permission of BSW.</li>
        <li>The User of this system is advised that they should obtain services of a design professional for the use of this product. BSW only represents that our product will withstand loading as documented in our specifications. The design professional shall evaluate the loading conditions and determine if the loading conditions fall within the parameters of the Collar system. Additionally, the user should employ the design professional to inspect the Pilings to ensure they are acceptable for use.</li>
        <li>Local Permitting may be required for use of this product. Consult with your local code official prior to use.</li>
        <li>The User of this system should employ installation contractors that have adequate skills for the required work. BSW does not and cannot attest to any skill set or quality of work of any installer.</li>
        <li>The written instructions for installation must be followed. Failure to do so could result in failure of the system.</li>
      </ol>
      <p class="standards__foot">
        PO Box 41920,<br>
        Harrow Ridge, PA 18990-0090<br>
        T. 610.555.0142 &nbsp;|&nbsp; F. 610.555.0187<br>
        Email: sales@brackenfieldworks.example<br>
        <span class="web">www.brackenfieldworks.example</span>
      </p>
    </div>
  </section>

</main>
</body>
</html>
```